Vehicle Signage Design for a Renovation Company

We're a renovation company specialising in Home Renovations. The final design should communicate trust, credibility, and confidence. We need vehicle signage designed for our company utes (see attachment) / for our grey ute with the canopy/ and white use withou the canopyI've also attached our existing designs for the current vehicles (van and hatch back) to give you an idea of what we're after.In terms of content, there isn't much requirement for this due to the limited space on the ute - but happy to hear ideas on this.We've tried designing it ourselves - see attachment, but not happy with the result, would like more variations and ideas.Check out our website www.kestrelrenovations.co.nz for ideas on our branding/ style.
Updates

Target Market(s)

Home Owners

Industry/Entity Type

Residential Construction

Font styles to use
Sans Serif

Colors
3276b5
0355a3
33a6d7
3aa7d7
ffffff

Requirements
Must have
• Logo, Call to Action (website and number), Headline
Nice to have
• Strong sharp lines, a clean/sleek look
• It would be nice to have our offer on there (free design plans) / but we know space is limited

```html
<!DOCTYPE html>
<html lang="en">
<head>
<meta charset="utf-8">
<title>Kestrel Home Renovations – Ute Side Wrap</title>
<link rel="stylesheet" href="https://fonts.googleapis.com/css2?family=Open+Sans:wght@400;600;700;800&family=Kaushan+Script&display=swap">
<style>
  :root {
    --navy: #0a2384;
    --royal: #0355a3;
    --brand-blue: #1e55c9;
    --bright-blue: #1a6fe0;
    --sky: #33a6d7;
    --silver: #e6e8ec;
    --silver-dark: #c9ccd2;
    --red: #e83a3f;
    --white: #ffffff;
    --ink: #1c1c22;
    --bg: #ffffff;
  }
  * { box-sizing: border-box; margin: 0; padding: 0; }
  html, body { width: 1200px; height: 723px; overflow: hidden; background: var(--bg); }
  .canvas { position: relative; width: 1200px; height: 723px; font-family: "Open Sans", Arial, sans-serif; }
  .wrap-art { position: absolute; left: 0; top: 0; }
  .txt { position: absolute; line-height: 1; white-space: nowrap; font-weight: 800; }
  .outlined { text-shadow: 0 0 2px #000, 1px 1px 2px rgba(0,0,0,.7); }

  .thinking { left: 148px; top: 345px; font-size: 17px; color: var(--bright-blue); text-align: center; line-height: 1.1;
    text-shadow: -1px -1px 0 #fff, 1px -1px 0 #fff, -1px 1px 0 #fff, 1px 1px 0 #fff; }
  .renovating { left: 128px; top: 384px; font-size: 15px; color: var(--white); text-align: center; line-height: 1.2; }

  .offer { left: 418px; top: 206px; text-align: center; color: var(--white); }
  .offer-free { font-size: 12px; font-weight: 600; display: block; margin-left: 40px; }
  .offer-script { font-family: "Kaushan Script", cursive; font-weight: 400; font-size: 36px; color: var(--red);
    display: block; margin-top: -4px; text-shadow: -1px -1px 0 #fff, 1px -1px 0 #fff, -1px 1px 0 #fff, 1px 1px 0 #fff; }
  .offer-build { font-size: 12px; font-weight: 700; display: block; margin-top: -2px; margin-left: 10px; }
  .offer-sub { font-size: 9px; font-weight: 400; font-style: italic; color: var(--sky); display: block; margin-top: 4px; }

  .headline { left: 480px; top: 393px; text-align: center; font-size: 27px; line-height: 1.1; }
  .headline .blue { color: var(--bright-blue); text-shadow: -1px -1px 0 #fff, 1px -1px 0 #fff, -1px 1px 0 #fff, 1px 1px 0 #fff; }
  .headline .white { color: var(--white); }

  .brand { left: 770px; top: 290px; color: var(--brand-blue); font-weight: 800; }
  .brand-name { display: block; font-size: 70px; letter-spacing: -1px; }
  .brand-tag { display: block; font-size: 16px; color: var(--brand-blue); margin-top: 6px; margin-left: 120px; letter-spacing: .5px; }

  .url-bar { position: absolute; left: 760px; top: 408px; width: 300px; height: 26px; background: var(--red);
    color: var(--white); font-size: 15px; font-weight: 700; display: flex; align-items: center; justify-content: center; letter-spacing: .3px; }
  .phone { left: 812px; top: 448px; font-size: 32px; color: var(--bright-blue); font-style: italic; letter-spacing: .5px; }
</style>
</head>
<body>
<main class="canvas">
  <svg class="wrap-art" width="1200" height="723" viewBox="0 0 1200 723" aria-hidden="false">
    <defs>
      <linearGradient id="silverSheen" x1="0" y1="0" x2="0" y2="1">
        <stop offset="0" stop-color="#f4f5f7"/>
        <stop offset="1" stop-color="#d6d9de"/>
      </linearGradient>
      <linearGradient id="interiorTone" x1="0" y1="0" x2="0" y2="1">
        <stop offset="0" stop-color="#b7b2a8"/>
        <stop offset=".55" stop-color="#8c7a63"/>
        <stop offset="1" stop-color="#4a3a2a"/>
      </linearGradient>
      <linearGradient id="kitchenTone" x1="0" y1="0" x2="0" y2="1">
        <stop offset="0" stop-color="#9aa0a6"/>
        <stop offset=".6" stop-color="#c9c2b4"/>
        <stop offset="1" stop-color="#8a6a48"/>
      </linearGradient>
    </defs>

    <!-- side panel base -->
    <rect class="panel-base" x="60" y="190" width="1080" height="320" fill="url(#silverSheen)"/>

    <!-- navy block over the tray -->
    <polygon class="navy-block" points="300,190 640,190 640,300 300,300" fill="var(--navy)"/>
    <polygon class="navy-stripe" points="330,300 430,190 455,190 355,300" fill="#dfe3ee"/>
    <polygon class="navy-stripe" points="370,300 470,190 495,190 395,300" fill="#dfe3ee"/>

    <!-- left photo panel -->
    <polygon class="photo-kitchen" role="img" aria-label="Photo of a renovated kitchen interior"
      points="70,480 70,395 170,300 320,450 320,480" fill="url(#kitchenTone)"/>
    <polyline class="chevron" points="70,362 170,262 345,437" fill="none" stroke="var(--royal)" stroke-width="20"/>
    <polyline class="chevron" points="70,330 170,230 310,370" fill="none" stroke="var(--brand-blue)" stroke-width="12"/>
    <polyline class="chevron-light" points="190,250 250,190 300,190" fill="none" stroke="#dfe3ee" stroke-width="16"/>

    <!-- centre photo panel -->
    <polygon class="photo-living" role="img" aria-label="Photo of a renovated open-plan living room"
      points="360,495 360,420 485,300 650,462 620,495" fill="url(#interiorTone)"/>
    <polyline class="chevron" points="338,408 485,262 683,460 650,495" fill="none" stroke="var(--royal)" stroke-width="18"/>
    <polyline class="chevron" points="350,360 520,190" fill="none" stroke="var(--brand-blue)" stroke-width="16"/>
    <polyline class="chevron" points="330,330 470,190" fill="none" stroke="var(--sky)" stroke-width="6"/>
    <polyline class="chevron" points="560,270 640,350" fill="none" stroke="var(--brand-blue)" stroke-width="10"/>
  </svg>

  <p class="txt thinking">THINKING<br>ABOUT</p>
  <p class="txt renovating outlined">RENOVATING YOUR<br>HOME?</p>

  <p class="txt offer outlined">
    <span class="offer-free">BOOK A FREE</span>
    <span class="offer-script">Design</span>
    <span class="offer-build">DESIGN TO &nbsp;BUILD</span>
    <span class="offer-sub">CONSTRUCTION</span>
  </p>

  <h2 class="txt headline">
    <span class="blue">TRUSTED</span><br>
    <span class="blue">HOME</span><span class="white outlined"> RENOVATION</span><br>
    <span class="white outlined">EXPERTS</span>
  </h2>

  <h1 class="txt brand">
    <span class="brand-name">Kestrel</span>
    <span class="brand-tag">HOME RENOVATIONS</span>
  </h1>
  <div class="url-bar">KESTRELRENOVATIONS.CO.NZ</div>
  <p class="txt phone">0800 555 014</p>
</main>
</body>
</html>
```